Human Resource Consulting practice needs a business card design

We need a business card design (double sided colour) for our Human Resource (HR) consulting practice in regional New South Wales, australia. Our business name is Staffwise Partners. We support small and medium business across the Mid North Coast of New South Wales by providing them with outsourced HR support, services and products to help them achieve compliance with workplace legislation and across all areas of the employment lifecycle from recruitment to termination and everything in between. Our corporate colours are hot pink and black. The final design should communicate professionalism, trust, people focus.
I have attached the current (old) business card for your reference.

Target Market(s)

Business owners and high level managers

Industry/Entity Type

Business

Contact Information for Business Card

Name
Title
Phone no
Mobile no
Address
PO Box
email address
website

Colors
e34197

Requirements
Must have
• Tempate for changing business card personal details including Name, position title, mobile number, email address.
• Keep current logo and colours as per attached
• Logo must be presented in 2 colours or black only not white
Nice to have
• One side logo and graphic only other side logo and personal details
Should not have
• Should not be the same as the current version (attached) but a modern interpretation.
• Does not need a busy reverse side with our list of services as per current version. I feel this is too busy.
• No photos

```html
<!DOCTYPE html>
<html lang="en">
<head>
<meta charset="utf-8">
<title>Staffwise Partners – Business Card</title>
<link href="https://fonts.googleapis.com/css2?family=Questrial&display=swap" rel="stylesheet">
<style>
  :root {
    --hot-pink: #e3198f;
    --ink: #0d0d0d;
    --paper: #f4f4f2;
    --stage: #e6e4e1;
    --text-dark: #1c1c1c;
    --text-light: #dddddd;
  }
  * { margin: 0; padding: 0; box-sizing: border-box; }
  html, body { width: 1200px; height: 900px; overflow: hidden; }
  body {
    background: var(--stage);
    font-family: "Questrial", "Century Gothic", sans-serif;
    position: relative;
  }
  .card {
    position: absolute;
    top: 291px;
    width: 520px;
    height: 318px;
    background: var(--paper);
    box-shadow: 0 6px 18px rgba(0,0,0,0.18);
    overflow: hidden;
  }
  .card--details { left: 50px; }
  .card--brand { left: 630px; }

  /* contact side */
  .name-band {
    position: absolute; left: 0; top: 22px; width: 100%; height: 96px;
    background: linear-gradient(90deg, var(--ink) 0%, var(--ink) 55%, #2a0a1e 80%, #4a0d33 100%);
  }
  .brand-glow {
    position: absolute; left: 300px; top: 70px; width: 220px; height: 110px;
  }
  .person {
    position: absolute; left: 150px; top: 42px; color: #fff;
  }
  .person__name { font-size: 24px; letter-spacing: 0.5px; }
  .person__title { font-size: 12px; margin-top: 2px; color: var(--text-light); }
  .wordmark {
    position: absolute; left: 330px; top: 110px;
    font-size: 21px; color: #fff; white-space: nowrap;
  }
  .contact {
    position: absolute; left: 70px; top: 140px;
    font-size: 13.5px; line-height: 21px; color: var(--text-dark);
  }
  .contact dt { display: inline-block; width: 70px; }
  .contact dd { display: inline; }
  .email-strip {
    position: absolute; left: 0; top: 246px; width: 280px; height: 24px;
    background: var(--hot-pink);
    clip-path: polygon(0 0, 100% 0, 95% 100%, 0 100%);
    font-size: 11.5px; line-height: 24px; padding-left: 16px; color: var(--ink);
    white-space: nowrap;
  }
  .web-band {
    position: absolute; left: 262px; top: 270px; width: 258px; height: 30px;
    background: var(--ink);
    border-bottom: 3px solid var(--hot-pink);
    clip-path: polygon(5% 0, 100% 0, 100% 100%, 0 100%);
    font-size: 11.5px; line-height: 28px; padding-left: 22px; color: var(--hot-pink);
    white-space: nowrap;
  }

  /* brand side */
  .brand-lockup {
    position: absolute; inset: 0;
    display: flex; align-items: center; justify-content: center;
    font-size: 30px; color: var(--text-dark);
  }
</style>
</head>
<body>

<section class="card card--details" aria-label="Business card, contact side">
  <div class="name-band"></div>
  <svg class="brand-glow" viewBox="0 0 220 110" aria-hidden="true">
    <defs>
      <radialGradient id="glow" cx="55%" cy="45%" r="60%">
        <stop offset="0%" stop-color="#e3198f"/>
        <stop offset="60%" stop-color="#8f1260"/>
        <stop offset="100%" stop-color="#2a0a1e" stop-opacity="0"/>
      </radialGradient>
    </defs>
    <ellipse cx="120" cy="55" rx="105" ry="48" fill="url(#glow)"/>
  </svg>
  <div class="person">
    <p class="person__name">Maren Holt</p>
    <p class="person__title">Principal Consultant</p>
  </div>
  <p class="wordmark">Staffwise Partners</p>
  <dl class="contact">
    <div>PO Box 218, Kendall Bay, NSW 2439</div>
    <div><dt>Phone #:</dt><dd>02 6500 3127</dd></div>
    <div><dt>Mobile #:</dt><dd>0400 555 018</dd></div>
    <div><dt>Fax</dt><dd>#: 02 6500 3199</dd></div>
  </dl>
  <p class="email-strip">email: maren@staffwisepartners.com.au</p>
  <p class="web-band">website: www.staffwisepartners.com.au</p>
</section>

<section class="card card--brand" aria-label="Business card, brand side">
  <p class="brand-lockup">Staffwise Partners</p>
</section>

</body>
</html>
```